Werbebrief
Zielgruppe
Unsere Zielgruppe sind Geschäftsführer junger Unternehmen.
Hallo,
Wir benötigen einen "Werbebrief". Es ist jedoch weniger ein Brief, als viel mehr eine etwas größerer "Werbekarte" (diese soll 105 x 210mm groß sein).
Auf der Vorderseite soll folgender Text stehen:
Für Unternehmen, die gerne expandieren möchten
Auf der Rückseite soll folgender Link stehen:
www.tolvek-werk.de/Expandieren
Darunter soll folgendes stehen:
Ihr persönlicher Code: ABC123
Wichtig ist, dass wir den Code individuell ändern können, da jeder einen anderen Code bekommt.
Unser Logo und Corporate Farbe habe ich hochgeladen. Das Design sollte auf jeden Fall zu unserer Webseite passen (www.tolvek-werk.de)
Wir freuen uns auf Ihre Vorschläge.

```html
<!DOCTYPE html>
<html lang="de">
<head>
<meta charset="utf-8">
<title>Tolvek Werk – Werbekarte</title>
<link rel="stylesheet" href="https://fonts.googleapis.com/css2?family=Carlito:wght@400&display=swap">
<style>
  :root {
    --page-bg: #e8e6e3;
    --card-blue-top: #2656a3;
    --card-blue-bottom: #1c468c;
    --card-text: #f3f6fb;
    --card-shadow: rgba(20, 30, 50, 0.28);
  }
  * { margin: 0; padding: 0; box-sizing: border-box; }
  html, body {
    width: 1200px;
    height: 1200px;
    overflow: hidden;
    background: var(--page-bg);
    font-family: "Carlito", "Calibri", sans-serif;
  }
  .canvas {
    position: relative;
    width: 1200px;
    height: 1200px;
  }
  .card {
    position: absolute;
    left: 170px;
    width: 874px;
    height: 438px;
    background: linear-gradient(180deg, var(--card-blue-top) 0%, var(--card-blue-bottom) 100%);
    box-shadow: 0 10px 24px var(--card-shadow);
    color: var(--card-text);
  }
  .card--front { top: 126px; }
  .card--back  { top: 624px; }

  .brand {
    position: absolute;
    top: 28px;
    right: 34px;
    display: flex;
    align-items: center;
    gap: 12px;
    font-size: 38px;
    line-height: 1;
    letter-spacing: 0.2px;
  }
  .brand__divider {
    width: 2px;
    height: 36px;
    background: var(--card-text);
  }

  .tagline {
    position: absolute;
    top: 178px;
    left: 136px;
    font-size: 36px;
    line-height: 52px;
  }
  .tagline__line { display: block; }
  .tagline__line--indent { padding-left: 189px; }

  .campaign-url {
    position: absolute;
    top: 124px;
    left: 52px;
    font-size: 31px;
  }
  .personal-code {
    position: absolute;
    right: 36px;
    bottom: 26px;
    font-size: 29px;
  }
</style>
</head>
<body>
<main class="canvas">
  <section class="card card--front" aria-label="Vorderseite">
    <div class="brand">
      <span class="brand__divider"></span>
      <span class="brand__name">Tolvek Werk</span>
    </div>
    <p class="tagline">
      <span class="tagline__line">Für Unternehmen, die gerne</span>
      <span class="tagline__line tagline__line--indent">expandieren möchten</span>
    </p>
  </section>

  <section class="card card--back" aria-label="Rückseite">
    <div class="brand">
      <span class="brand__divider"></span>
      <span class="brand__name">Tolvek Werk</span>
    </div>
    <p class="campaign-url">www.tolvek-werk.de/Expandieren</p>
    <p class="personal-code">Ihr persönlicher Code: Tol1612</p>
  </section>
</main>
</body>
</html>
```